I require a complete design for a responsive 3 page business website.

High end design type, similar to (in order of preference):
]https://brennalofts.co/
https://renewing-pathways-guidance.com.au/
https://quietridgementoring.com.au/
https://buildakindday.com/
https://thecalmfieldguide.com/
https://www.dalekestrel.com/
https://thepivot.com/

Please use the attached old company logo, which is to be used a reference for the new branding and design.

Please use the colour palette below
#3D3D3D
#FBF8F3
#CAAD53
#7EB492
#EDCFBF
Updates

Provided feedback to top 3 designs, now waiting on amended iterations.

Target Market(s)

Male & female 30-50s, small business owners and executive corporates, first world english speaking nations.

Industry/Entity Type

Life Coaching

Logo Text

Willow Compass Path. Tagline: Holistic Transformational Coaching

Number of Pages Required

3 page

Font styles to use
Sans Serif

Requirements
Must have
• Testimonials section, google reivews section, book online button.

```html
<!DOCTYPE html>
<html lang="en">
<head>
<meta charset="utf-8">
<title>Willow Compass Path – Holistic Transformational Coaching</title>
<link rel="stylesheet" href="https://fonts.googleapis.com/css2?family=Playfair+Display:wght@400&family=Poppins:wght@400;500;600&display=swap">
<style>
:root{
  --ink:#3d3d3d;
  --cream:#fbf8f3;
  --gold:#caad53;
  --sage:#7eb492;
  --blush:#edcfbf;
  --blush-light:#fbf1ec;
  --hero-grey:#ebebe9;
  --muted:#7a7a7a;
  --line:#e3e3e3;
  --footer-field:#333333;
}
*{box-sizing:border-box;margin:0;padding:0}
html,body{width:1200px;height:4812px;overflow:hidden}
body{font-family:"Poppins",sans-serif;color:var(--ink);background:#fff;position:relative}
.section{position:absolute;left:0;width:1200px}
.abs{position:absolute}
.serif-title{font-family:"Playfair Display",serif;color:var(--gold);text-transform:uppercase;font-weight:400;letter-spacing:1px}
.center-title{position:absolute;left:0;width:1200px;text-align:center;font-size:34px;line-height:1}
.center-sub{position:absolute;left:0;width:1200px;text-align:center;font-size:15px;letter-spacing:1px;color:var(--ink)}
.btn{position:absolute;display:flex;align-items:center;gap:10px;border-radius:20px;color:#fff;font-size:11px;font-weight:600;text-transform:uppercase;padding-left:8px;letter-spacing:.3px;white-space:nowrap}
.btn .star{width:24px;height:24px;border-radius:50%;border:1.5px solid #fff;display:flex;align-items:center;justify-content:center;font-size:11px}
.btn-sage{background:var(--sage)}
.btn-gold{background:var(--gold)}
.btn-ink{background:var(--ink)}
.btn-white{background:#fff;color:var(--ink)}
.btn-white .star{border-color:var(--sage);color:var(--sage)}
.photo{position:absolute}
.small{font-size:10.5px;line-height:21px;color:var(--muted)}

/* header */
.site-header{top:0;height:79px;background:#fff;box-shadow:0 2px 6px rgba(0,0,0,.06);z-index:2}
.brand{position:absolute;display:flex;align-items:center;gap:9px}
.brand-mark{width:32px;height:32px;border-radius:50%;border:2px solid var(--gold);flex:none}
.brand-name{font-size:20px;font-weight:600;color:var(--gold);line-height:1;letter-spacing:.3px;white-space:nowrap}
.brand-tag{font-size:9px;color:var(--gold);margin-top:3px;white-space:nowrap}
.nav a{position:absolute;top:31px;font-size:12.5px;color:var(--ink);text-decoration:none}
.nav a.active{color:var(--gold)}
.sign-in{position:absolute;left:970px;top:22px;width:120px;height:34px;border-radius:17px;background:var(--gold);color:#fff;font-size:12px;font-weight:600;display:flex;align-items:center;justify-content:center;gap:8px}

/* hero */
.hero{top:79px;height:501px;background:var(--hero-grey)}
.hero-title{position:absolute;left:108px;top:168px;font-size:52px;line-height:1}
.hero-sub{position:absolute;left:108px;top:232px;font-size:26px;letter-spacing:1.5px;line-height:1.2}
.dot{position:absolute;left:50px;width:9px;height:9px;border-radius:50%;border:1px solid #999}
.dot.on{background:var(--gold);border-color:var(--gold)}

/* service cards */
.card{position:absolute;width:243px;height:250px;border:1px solid var(--line);text-align:center;background:#fff}
.card.featured{background:var(--sage);border-color:var(--sage)}
.card.featured h3,.card.featured p{color:#fff}
.card .icon{width:58px;height:58px;border-radius:50%;margin:22px auto 0;display:flex;align-items:center;justify-content:center}
.card h3{font-size:12.5px;font-weight:600;line-height:19px;margin-top:22px}
.card p{font-size:10px;line-height:21px;color:var(--muted);margin:8px 18px 0}

/* blog */
.post{position:absolute;background:#fff;box-shadow:0 2px 10px rgba(0,0,0,.08)}
.post-date{font-size:10.5px;color:var(--muted)}
.post h4{font-size:12.5px;font-weight:600;line-height:17px;margin-top:8px}
.post p{font-size:10px;line-height:21px;color:var(--muted);margin-top:10px}

/* reviews */
.review-bar{position:absolute;left:385px;top:410px;width:430px;height:44px;border:1px solid var(--blush);border-radius:22px;background:var(--cream);display:flex;align-items:center;justify-content:center;gap:12px;font-size:12px}
.review-bar .score{font-weight:600;color:var(--ink)}
.review-bar .stars{color:var(--gold);letter-spacing:1px}
.review-bar .count{color:var(--muted);font-size:11px}

/* footer */
.site-footer{top:4471px;height:341px;background:var(--ink);color:#fff}
.site-footer h5{position:absolute;font-size:16px;font-weight:500;letter-spacing:.5px}
.foot-link{position:absolute;font-size:11px;color:#ddd}
.social{position:absolute;top:126px;width:30px;height:30px;border-radius:50%;background:var(--cream)}
.field{position:absolute;left:877px;width:213px;height:38px;background:var(--footer-field);border:1px solid #5a5a5a;font-size:10.5px;color:#bbb;padding:11px 14px}
</style>
</head>
<body>

<header class="section site-header">
  <div class="brand" style="left:108px;top:22px">
    <span class="brand-mark"></span>
    <div><div class="brand-name">WILLOW COMPASS PATH</div><div class="brand-tag">Holistic Transformational Coaching</div></div>
  </div>
  <nav class="nav">
    <a class="active" style="left:501px">Home</a>
    <a style="left:566px">About Us</a>
    <a style="left:649px">Services</a>
    <a style="left:727px">Blog</a>
    <a style="left:783px">Testimonials</a>
    <a style="left:888px">Contact</a>
  </nav>
  <div class="sign-in"><svg width="13" height="13" viewBox="0 0 12 12"><circle cx="6" cy="3.5" r="2.8" fill="#fff"/><path d="M0.5 12c0-3.5 2.5-5 5.5-5s5.5 1.5 5.5 5z" fill="#fff"/></svg>Sign In</div>
</header>

<section class="section hero">
  <div class="photo" role="img" aria-label="Photo of a smiling senior mother hugging her adult daughter" style="left:529px;top:0;width:671px;height:501px;background:linear-gradient(120deg,#dedad4 0%,#c4b2a3 40%,#9aa6b8 70%,#d8d0c6 100%)"></div>
  <span class="dot" style="top:222px"></span><span class="dot on" style="top:241px"></span><span class="dot" style="top:259px"></span><span class="dot" style="top:278px"></span>
  <h1 class="serif-title hero-title">Start Living</h1>
  <p class="hero-sub">The Life Deserve To Live</p>
  <div class="btn btn-sage" style="left:108px;top:282px;width:225px;height:37px"><span class="star">★</span>Book Appointmnet Now</div>
</section>

<section class="section" style="top:580px;height:536px;background:#fff">
  <svg class="abs" style="left:222px;top:75px" width="400" height="380" viewBox="0 0 400 380">
    <circle cx="200" cy="190" r="180" fill="none" stroke="var(--sage)" stroke-width="7" stroke-dasharray="420 1131" transform="rotate(-120 200 190)" stroke-linecap="round"/>
    <circle cx="194" cy="196" r="180" fill="none" stroke="var(--blush)" stroke-width="6" stroke-dasharray="520 1131" transform="rotate(70 194 196)" stroke-linecap="round"/>
  </svg>
  <div class="photo" role="img" aria-label="Portrait of the coach, a woman with glasses and crossed arms" style="left:254px;top:97px;width:336px;height:336px;border-radius:50%;background:radial-gradient(circle at 50% 40%,#ece8e3,#cbc5be)"></div>
  <h2 class="serif-title abs" style="left:669px;top:116px;font-size:32px;line-height:1">About Us</h2>
  <p class="abs" style="left:669px;top:153px;font-size:15px;letter-spacing:1px">Hi, I am Mira Holt</p>
  <p class="abs small" style="left:669px;top:191px;width:300px">Lorem ipsum dolor sit amet, consectetur adipiscing elit. Duis eu dui vitae lectus feugiat maximus in sit amet jus Praesent vulputate nibh libero, id ullamcorper purus int erdum vel. Cras enim tortor, sollicitudin et ligula non, co ndimentum sagittis ante.</p>
  <p class="abs small" style="left:669px;top:311px;width:300px">Proin nibh ligula, dictum nec sagittis ut, sodales vel libe Cras sollicitudin velit ante, a ornare felis faucibus at.</p>
  <div class="btn btn-ink" style="left:669px;top:373px;width:135px;height:38px"><span class="star">★</span>Read More</div>
</section>

<section class="section" style="top:1116px;height:469px;background:var(--blush-light)">
  <h2 class="serif-title center-title" style="top:60px">How It Works</h2>
  <p class="center-sub" style="top:98px">Step 3</p>
  <div class="photo" role="img" aria-label="Photo of a man reading a tablet" style="left:265px;top:154px;width:132px;height:132px;border-radius:50%;background:linear-gradient(135deg,#d6cdc2,#8a7d70)"></div>
  <div class="photo" role="img" aria-label="Photo of a woman attending an online lecture" style="left:534px;top:166px;width:132px;height:132px;border-radius:50%;background:linear-gradient(135deg,#c2a78e,#76604f)"></div>
  <div class="photo" role="img" aria-label="Photo of a happy senior couple" style="left:801px;top:154px;width:132px;height:132px;border-radius:50%;background:linear-gradient(135deg,#ddd6cd,#958a7f)"></div>
  <svg class="abs" style="left:432px;top:210px" width="70" height="20"><path d="M2 12 Q35 0 66 12" fill="none" stroke="#999" stroke-dasharray="3 3"/><path d="M60 8 L66 12 L59 15" fill="none" stroke="#999"/></svg>
  <svg class="abs" style="left:700px;top:210px" width="70" height="20"><path d="M2 12 Q35 18 66 8" fill="none" stroke="#999" stroke-dasharray="3 3"/><path d="M59 5 L66 8 L60 13" fill="none" stroke="#999"/></svg>
  <p class="abs" style="left:231px;top:306px;width:200px;text-align:center;font-size:12.5px;font-weight:500">Book Your Appointment</p>
  <p class="abs" style="left:500px;top:319px;width:200px;text-align:center;font-size:12.5px;font-weight:500">Start Lecture</p>
  <p class="abs" style="left:767px;top:306px;width:200px;text-align:center;font-size:12.5px;font-weight:500">Enjoy Your Life</p>
  <div class="btn btn-sage" style="left:512px;top:364px;width:176px;height:38px"><span class="star">★</span>Get Started Now</div>
</section>

<section class="section" style="top:1585px;height:845px;background:#fff">
  <h2 class="serif-title center-title" style="top:78px">Our Service</h2>
  <p class="center-sub" style="top:114px">What We can Do For You</p>
  <div class="card" style="left:209px;top:168px"><div class="icon" style="background:var(--gold)"><svg width="24" height="24"><rect x="5" y="4" width="14" height="16" rx="3" fill="#fff"/></svg></div><h3>Healthy Mind &amp; Body<br>Life Coaching</h3><p>Lorem ipsum dolor amet, consectet ur adipiscing elit. Duis eu dui vitae lect feugiat maximus in sit amet justo. Praesent vulputate nibh libero.</p></div>
  <div class="card featured" style="left:478px;top:168px"><div class="icon" style="background:#fff"><svg width="24" height="24"><circle cx="12" cy="7" r="4" fill="var(--sage)"/><rect x="4" y="13" width="16" height="8" fill="var(--sage)"/></svg></div><h3>Life Coaching<br>Consultation</h3><p>Lorem ipsum dolor amet, consectet ur adipiscing elit. Duis eu dui vitae lect feugiat maximus in sit amet justo. Praesent vulputate nibh libero.</p></div>
  <div class="card" style="left:746px;top:168px"><div class="icon" style="background:var(--ink)"><svg width="24" height="24"><circle cx="10" cy="7" r="4" fill="#fff"/><rect x="3" y="13" width="18" height="8" rx="2" fill="#fff"/></svg></div><h3>Career Analysis<br>life coaching</h3><p>Lorem ipsum dolor amet, consectet ur adipiscing elit. Duis eu dui vitae lect feugiat maximus in sit amet justo. Praesent vulputate nibh libero.</p></div>
  <div class="card" style="left:209px;top:443px"><div class="icon" style="background:var(--blush)"><svg width="24" height="24"><circle cx="12" cy="12" r="9" fill="var(--ink)"/><line x1="12" y1="4" x2="12" y2="20" stroke="var(--blush)" stroke-width="2"/></svg></div><h3>Mind Your Behaviour<br>Life Coaching</h3><p>Lorem ipsum dolor amet, consectet ur adipiscing elit. Duis eu dui vitae lect feugiat maximus in sit amet justo. Praesent vulputate nibh libero.</p></div>
  <div class="card" style="left:478px;top:443px"><div class="icon" style="background:var(--gold)"><svg width="24" height="24"><rect x="3" y="5" width="18" height="12" fill="#fff"/><rect x="8" y="18" width="8" height="2" fill="#fff"/></svg></div><h3>Online<br>Life Coaching</h3><p>Lorem ipsum dolor amet, consectet ur adipiscing elit. Duis eu dui vitae lect feugiat maximus in sit amet justo. Praesent vulputate nibh libero.</p></div>
  <div class="card" style="left:746px;top:443px"><div class="icon" style="background:var(--sage)"><svg width="24" height="24"><circle cx="12" cy="8" r="5" fill="#fff"/><rect x="5" y="15" width="14" height="6" rx="2" fill="#fff"/></svg></div><h3>Hypnosis for Anxiety,<br>Addictions &amp; Habits</h3><p>Lorem ipsum dolor amet, consectet ur adipiscing elit. Duis eu dui vitae lect feugiat maximus in sit amet justo. Praesent vulputate nibh libero.</p></div>
  <div class="btn btn-gold" style="left:512px;top:727px;width:176px;height:38px"><span class="star">★</span>Get Started Now</div>
</section>

<section class="section" style="top:2430px;height:284px;background:var(--sage);color:#fff">
  <h2 class="center-title" style="top:64px;font-family:'Playfair Display',serif;font-size:28px;letter-spacing:1px">ARE YOU READY TO MAKE 2021 YOUR YEAR ?</h2>
  <p class="abs" style="left:0;top:108px;width:1200px;text-align:center;font-size:13.5px;line-height:22px">Close the &nbsp;Gap Between Where You are Today - and Where You Want to be My Way<br>of Life Coaching is to Empower You to Become the Best Version of Yourself Inside and Out.</p>
  <div class="btn btn-white" style="left:525px;top:181px;width:148px;height:38px"><span class="star">★</span>Book Online</div>
</section>

<section class="section" style="top:2714px;height:589px;background:#fff">
  <h2 class="serif-title abs" style="left:174px;top:142px;font-size:34px;line-height:1">Coaching</h2>
  <p class="abs" style="left:174px;top:183px;font-size:15px;letter-spacing:1px">For Women Life</p>
  <p class="abs small" style="left:174px;top:214px;width:295px">Fusce egestas tristique nunc, sed semper velit viverra et. Pellentesque at ex elementum, fermentum magna at, congue ex. Duis nec dignissim arcu. Nam nulla purs ultricies id tellus vel, vestibulum facilisis purus. Vestibu lum molestie turpis mattis euismod.</p>
  <p class="abs small" style="left:174px;top:334px;width:295px">Morbi ac ipsum sit amet erat sagittis ullamcorper vita e eget lorem. Etiam ac dapibus dolor. Curabitur finibus mauris eu posuere vehicula.</p>
  <div class="btn btn-gold" style="left:176px;top:420px;width:175px;height:38px"><span class="star">★</span>Get Started Now</div>
  <div class="photo" role="img" aria-label="Portrait of a smiling senior woman with glasses" style="left:617px;top:165px;width:336px;height:336px;border-radius:50%;background:radial-gradient(circle at 50% 40%,#e9e0d7,#b3ada7)"></div>
  <div class="abs" style="left:748px;top:112px;width:66px;height:66px;border-radius:50%;background:var(--ink);border:3px solid #fff"></div>
  <div class="abs" style="left:594px;top:396px;width:66px;height:66px;border-radius:50%;background:var(--gold);border:3px solid #fff"></div>
  <div class="abs" style="left:902px;top:396px;width:66px;height:66px;border-radius:50%;background:var(--sage);border:3px solid #fff"></div>
  <p class="abs" style="left:844px;top:100px;font-size:13px;line-height:19px">Career<br>Coaching</p>
  <p class="abs" style="left:506px;top:470px;font-size:13px;line-height:19px">Transformational<br>Training</p>
  <p class="abs" style="left:968px;top:455px;font-size:13px;line-height:19px">Online<br>Courses</p>
  <svg class="abs" style="left:798px;top:80px" width="40" height="30"><path d="M6 4 Q24 6 22 26" fill="none" stroke="#aaa"/></svg>
  <svg class="abs" style="left:612px;top:470px" width="40" height="30"><path d="M34 2 Q36 24 14 26" fill="none" stroke="#aaa"/></svg>
  <svg class="abs" style="left:930px;top:470px" width="40" height="30"><path d="M6 2 Q4 24 26 26" fill="none" stroke="#aaa"/></svg>
</section>

<section class="section" style="top:3303px;height:691px;background:var(--cream)">
  <h2 class="serif-title center-title" style="top:60px">Our Blog</h2>
  <p class="center-sub" style="top:100px">Latest Blog &amp; News</p>
  <div class="post" style="left:209px;top:151px;width:333px;height:400px">
    <div class="photo" role="img" aria-label="Photo of an older couple embracing on a sofa" style="left:0;top:0;width:333px;height:213px;background:linear-gradient(135deg,#dcd3c9,#978676)"></div>
    <div class="abs" style="left:32px;top:234px;width:275px"><div class="post-date">20 Feb 2021</div><h4>Lorem ipsum dolor sit amet, conse tetur adipiscing elit</h4><p>Lorem ipsum dolor sit amet, consectetur adipisc ing elit. Nullam euismod lectus id blandit pellent esque. Quisque tincidunt facilisis eros, eget viver a massa venenatis vitae.</p></div>
  </div>
  <div class="post" style="left:563px;top:151px;width:426px;height:191px">
    <div class="photo" role="img" aria-label="Photo of two women talking in a counselling session" style="left:0;top:0;width:166px;height:191px;background:linear-gradient(135deg,#d0c4b3,#857566)"></div>
    <div class="abs" style="left:179px;top:18px;width:230px"><div class="post-date">10 Jan 2021</div><h4>Lorem ipsum dolor sit amet, conse tetur adipiscing elit</h4><p>Lorem ipsum dolor sit amet, consectetur ing elit. Nullam euismod lectus id blandit esque. Quisque tincidunt facilisis eros, eg a massa venenatis vitae.</p></div>
  </div>
  <div class="post" style="left:563px;top:360px;width:426px;height:191px">
    <div class="photo" role="img" aria-label="Photo of a mother hugging her young son" style="left:0;top:0;width:166px;height:191px;background:linear-gradient(135deg,#cdbba7,#d2ab55 60%,#94796a)"></div>
    <div class="abs" style="left:179px;top:18px;width:230px"><div class="post-date">25 Jan 2021</div><h4>Lorem ipsum dolor sit amet, conse tetur adipiscing elit</h4><p>Lorem ipsum dolor sit amet, consectetur ing elit. Nullam euismod lectus id blandit esque. Quisque tincidunt facilisis eros, eg a massa venenatis vitae.</p></div>
  </div>
  <div class="btn btn-sage" style="left:536px;top:587px;width:128px;height:37px"><span class="star">★</span>View All</div>
</section>

<section class="section" style="top:3994px;height:477px;background:#fff">
  <h2 class="serif-title center-title" style="top:70px">Testimonial</h2>
  <p class="center-sub" style="top:109px">What Our Customer Says</p>
  <svg class="abs" style="left:500px;top:190px" width="20" height="44"><path d="M16 2 L4 22 L16 42" fill="none" stroke="#999"/></svg>
  <svg class="abs" style="left:680px;top:190px" width="20" height="44"><path d="M4 2 L16 22 L4 42" fill="none" stroke="#999"/></svg>
  <div class="abs" style="left:545px;top:158px;width:110px;height:110px;border-radius:50%;border:3px solid var(--sage);border-bottom-color:var(--gold)"></div>
  <div class="photo" role="img" aria-label="Portrait of the reviewing client" style="left:554px;top:167px;width:92px;height:92px;border-radius:50%;background:linear-gradient(135deg,#cfae98,#7a5947)"></div>
  <p class="abs" style="left:0;top:278px;width:1200px;text-align:center;font-size:12.5px;font-weight:600">Elena Voss</p>
  <p class="abs" style="left:0;top:297px;width:1200px;text-align:center;font-size:11px;color:var(--gold);letter-spacing:1px">★★★★★</p>
  <p class="abs" style="left:272px;top:300px;font-family:'Playfair Display',serif;font-size:40px;line-height:1;color:#bbb">“</p>
  <p class="abs" style="left:270px;top:318px;width:660px;text-align:center;font-size:10.5px;line-height:21px;color:var(--muted)">Sed bibendum diam sit amet lectus placerat consequat. Integer iaculis euismod neque id euismod. Donec nec fringilla mauris. Duis a molestie mi. Etiam pharetra ac dui nec dictum. Ut arcu quam, pharetra quis eros vitae dolor vitae tellus sagittis pellentesque. Nunc molestie aliquet lacus eget placerat.</p>
  <p class="abs" style="left:902px;top:370px;font-family:'Playfair Display',serif;font-size:40px;line-height:1;color:#bbb">”</p>
  <div class="review-bar"><span class="score">Verified Client Reviews</span><span class="stars">★★★★★</span><span class="score">4.9 / 5</span><span class="count">from 128 reviews</span></div>
</section>

<footer class="section site-footer">
  <div class="brand" style="left:108px;top:62px">
    <span class="brand-mark"></span>
    <div><div class="brand-name" style="font-size:17px">WILLOW COMPASS PATH</div><div class="brand-tag" style="color:#eee;font-size:8.5px">Holistic Transformational Coaching</div></div>
  </div>
  <span class="social" style="left:150px"></span>
  <span class="social" style="left:190px"></span>
  <span class="social" style="left:230px"></span>
  <span class="social" style="left:270px"></span>
  <h5 style="left:428px;top:64px">Contact Us</h5>
  <svg class="abs" style="left:428px;top:96px" width="14" height="18"><path d="M7 17 C2 10 1 8 1 6 a6 6 0 0 1 12 0 c0 2-1 4-6 11z" fill="#fff"/><circle cx="7" cy="6" r="2" fill="var(--ink)"/></svg>
  <p class="foot-link" style="left:454px;top:98px;font-size:10px;line-height:16px">Your Location Name Will Be<br>Here Near This 123456</p>
  <svg class="abs" style="left:428px;top:147px" width="14" height="14"><path d="M2 3 Q3 1 5 2 L6 5 L4 6 Q6 9 8 10 L9 8 L12 9 Q13 11 11 12 Q4 12 2 3z" fill="#fff"/></svg>
  <p class="foot-link" style="left:454px;top:146px;font-weight:600;color:#fff">555-014-2287</p>
  <svg class="abs" style="left:428px;top:180px" width="16" height="12"><rect x="0.5" y="0.5" width="15" height="11" fill="#fff"/><path d="M1 1 L8 7 L15 1" fill="none" stroke="var(--ink)"/></svg>
  <p class="foot-link" style="left:454px;top:178px;font-size:10px">hello@willowcompasspath.co</p>
  <h5 style="left:688px;top:64px">Quick Links</h5>
  <p class="foot-link" style="left:688px;top:98px">›&nbsp; Home</p>
  <p class="foot-link" style="left:688px;top:124px">›&nbsp; About</p>
  <p class="foot-link" style="left:688px;top:148px">›&nbsp; Service</p>
  <p class="foot-link" style="left:688px;top:174px">›&nbsp; Blog</p>
  <p class="foot-link" style="left:688px;top:198px">›&nbsp; Testimonial</p>
  <p class="foot-link" style="left:688px;top:225px">›&nbsp; Contact</p>
  <h5 style="left:877px;top:64px">News Letter</h5>
  <div class="field" style="top:97px">Name*</div>
  <div class="field" style="top:144px">Email*</div>
  <div class="btn btn-sage" style="left:877px;top:192px;width:145px;height:37px"><span class="star">★</span>Submit Now</div>
  <p class="abs" style="left:0;top:315px;width:1200px;text-align:center;font-size:10px;color:#ccc">©2021 Copyright Willow Compass Path Holistic Transformational Coaching. All Rights Reserved</p>
</footer>

</body>
</html>
```